Invite Card (Ministers) (business cards used for personal invitation to our church)

I need a business card sized advertisement. The card is a replacement for the attached card only much much cooler. I do not want a image background but more of a vectored, flat look with advertising colors.

I have attached a new image of the couple to replace the old image and a new logo to replace the old logo.

I need a PSD with ALL of the layers un-merged & unlocked

The back of the card should carry the same information as the old card.

Use advertising color and a modern flat look and feel.

Target Market(s)

professional audience

Industry/Entity Type

Non-Profit

Contact Information for Business Card

The card is a replacement for the attached card only much much cooler. I do not want a image background but more of a vectored, flat look with advertising colors.

Font styles to use
Sans Serif

Requirements
Must have
• Must have new logo, new image of couple
Should not have
• graphical background

```html
<!DOCTYPE html>
<html lang="en">
<head>
<meta charset="utf-8">
<title>Grace Commons – Invite Card</title>
<link href="https://fonts.googleapis.com/css2?family=Cinzel:wght@400;700&family=Great+Vibes&display=swap" rel="stylesheet">
<style>
  :root {
    --page-bg: #e9ebee;
    --blue-deep: #1577c9;
    --blue-mid: #1e9ee0;
    --blue-light: #35bdea;
    --ink-navy: #0d2a4a;
    --white: #ffffff;
    --silver-light: #f2f3f5;
    --silver-dark: #a9adb3;
    --photo-green: #d3e66e;
    --photo-blue: #3bb6e4;
    --photo-teal: #7fd0d8;
  }
  html, body {
    margin: 0;
    width: 1200px;
    height: 900px;
    overflow: hidden;
    background: var(--page-bg);
  }
  .canvas {
    position: relative;
    width: 1200px;
    height: 900px;
  }
  .card {
    position: absolute;
    width: 560px;
    height: 320px;
    border-radius: 4px;
    overflow: hidden;
    box-shadow: 0 10px 26px rgba(0,0,0,0.25);
  }
  .card-back {
    left: 70px;
    top: 90px;
    background:
      linear-gradient(115deg, transparent 0 38%, rgba(255,255,255,0.10) 38% 52%, transparent 52% 68%, rgba(255,255,255,0.08) 68% 80%, transparent 80%),
      linear-gradient(100deg, var(--blue-deep) 0%, var(--blue-mid) 50%, var(--blue-light) 100%);
    color: var(--ink-navy);
    font-family: "Cinzel", serif;
  }
  .contact {
    text-align: center;
    margin-top: 32px;
    line-height: 1.5;
  }
  .contact .website { font-size: 15px; letter-spacing: 1px; }
  .contact .address { font-size: 17px; font-weight: 700; letter-spacing: 0.5px; }
  .contact .phone { font-size: 16px; letter-spacing: 1px; }
  .schedule {
    list-style: none;
    margin: 44px 40px 0;
    padding: 0;
  }
  .schedule li {
    display: flex;
    align-items: baseline;
    font-size: 16px;
    font-weight: 700;
    letter-spacing: 1px;
    margin-bottom: 16px;
  }
  .schedule .leader {
    flex: 1;
    border-bottom: 2px dotted var(--ink-navy);
    margin: 0 4px;
    transform: translateY(-4px);
  }
  .schedule .time { font-weight: 400; }
  .card-front {
    left: 570px;
    top: 480px;
  }
  .card-front svg { display: block; }
  .brand-name {
    font-family: "Cinzel", serif;
    font-weight: 700;
    font-size: 24px;
    fill: var(--white);
  }
  .invite-script {
    font-family: "Great Vibes", cursive;
    font-size: 42px;
    fill: var(--white);
  }
  .pastor-names {
    font-family: "Cinzel", serif;
    font-size: 12px;
    letter-spacing: 1px;
    fill: var(--ink-navy);
  }
</style>
</head>
<body>
<main class="canvas">

  <section class="card card-back" aria-label="Card back">
    <div class="contact">
      <div class="website">GRACECOMMONS.ORG</div>
      <div class="address">2280 W. Harbor Lane - Millbrook, TX 75099</div>
      <div class="phone">1-800-555-0142</div>
    </div>
    <ul class="schedule">
      <li><span class="day">Sunday</span><span class="leader"></span><span class="time">9.00 A.M</span></li>
      <li><span class="day">Sunday</span><span class="leader"></span><span class="time">11.00 A.M</span></li>
      <li><span class="day">Wed. Bible Class</span><span class="leader"></span><span class="time">7.00 P.M</span></li>
    </ul>
  </section>

  <section class="card card-front" aria-label="Card front">
    <svg width="560" height="320" viewBox="0 0 560 320">
      <defs>
        <linearGradient id="front-bg" x1="0" y1="0" x2="1" y2="0.3">
          <stop offset="0" stop-color="var(--blue-deep)"/>
          <stop offset="0.55" stop-color="var(--blue-mid)"/>
          <stop offset="1" stop-color="var(--blue-light)"/>
        </linearGradient>
        <linearGradient id="photo-fill" x1="0" y1="1" x2="0.9" y2="0">
          <stop offset="0" stop-color="var(--photo-blue)"/>
          <stop offset="0.5" stop-color="var(--photo-teal)"/>
          <stop offset="1" stop-color="var(--photo-green)"/>
        </linearGradient>
        <linearGradient id="silver" x1="0" y1="0" x2="0.4" y2="1">
          <stop offset="0" stop-color="var(--silver-light)"/>
          <stop offset="0.5" stop-color="var(--silver-dark)"/>
          <stop offset="1" stop-color="var(--silver-light)"/>
        </linearGradient>
        <linearGradient id="name-band" x1="0" y1="0" x2="1" y2="0">
          <stop offset="0" stop-color="var(--silver-dark)"/>
          <stop offset="0.6" stop-color="var(--silver-light)"/>
          <stop offset="1" stop-color="var(--silver-dark)"/>
        </linearGradient>
      </defs>

      <rect class="front-background" width="560" height="320" fill="url(#front-bg)"/>
      <polygon class="accent-stripe" points="400,0 470,0 380,320 310,320" fill="rgba(255,255,255,0.07)"/>
      <polygon class="accent-stripe" points="500,0 540,0 450,320 410,320" fill="rgba(255,255,255,0.06)"/>

      <path class="photo-ring" d="M0,0 H264 C350,34 366,190 342,320 H0 Z" fill="url(#silver)"/>
      <path class="photo-area" d="M0,0 H248 C334,34 350,190 326,320 H0 Z" fill="url(#photo-fill)"
            role="img" aria-label="Photo of the pastor couple"/>

      <rect class="name-band" x="0" y="272" width="336" height="26" fill="url(#name-band)" opacity="0.92"/>
      <text class="pastor-names" x="18" y="290">PASTOR SAMUEL &amp; RENEE WHITFIELD</text>

      <rect class="brand-mark" x="396" y="62" width="18" height="18" fill="var(--white)"/>
      <text class="brand-name" x="422" y="80">GRACE</text>
      <text class="brand-name" x="396" y="112">COMMONS</text>

      <text class="invite-script" x="378" y="185">You’re</text>
      <text class="invite-script" x="418" y="226">Invited</text>
    </svg>
  </section>

</main>
</body>
</html>
```